Stationery Design needed for logo design project

This project is linked to Logo: brand identity for modern furniture design studio..

Our company needs a Stationery Design. Please refer to our original project in the link above.

```html
<!DOCTYPE html>
<html lang="en">
<head>
<meta charset="utf-8">
<title>Vardel Stationery</title>
<link href="https://fonts.googleapis.com/css2?family=Source+Sans+3:wght@400&family=Jost:wght@300&family=Allura&display=swap" rel="stylesheet">
<style>
  :root {
    --backdrop: #cfcfcf;
    --paper: #ffffff;
    --ink: #2b2b2b;
    --ink-soft: #444444;
    --band: #3c3c3c;
    --rule: #777777;
    --script: #666666;
  }
  * { margin: 0; padding: 0; box-sizing: border-box; }
  html, body { width: 1200px; height: 751px; overflow: hidden; }
  body {
    position: relative;
    background: var(--backdrop);
    font-family: "Source Sans 3", "Segoe UI", sans-serif;
    color: var(--ink);
  }
  .sheet { position: absolute; background: var(--paper); }
  .band { position: absolute; left: 0; right: 0; background: var(--band); }

  .brand-name {
    position: absolute;
    font-family: "Jost", sans-serif;
    font-weight: 300;
    color: var(--ink);
    line-height: 1;
    letter-spacing: 1px;
  }

  .contact { position: absolute; list-style: none; font-size: 7.8px; color: var(--ink-soft); }
  .contact li { display: flex; align-items: center; height: 13px; white-space: nowrap; }
  .contact .bar { width: 1px; height: 9px; background: var(--ink); margin-right: 6px; }
  .contact svg { width: 9px; height: 9px; margin-right: 7px; flex: none; }

  /* Letterhead */
  .letterhead { left: 44px; top: 26px; width: 544px; height: 709px; }
  .letterhead .band-top { top: 0; height: 7px; }
  .letterhead .band-bottom { bottom: 0; height: 17px; }
  .letterhead .brand-name { left: 58px; top: 60px; font-size: 64px; }
  .letterhead .contact { left: 343px; top: 63px; }
  .letter-content { position: absolute; left: 28px; top: 202px; width: 490px; }
  .letter-body { font-size: 11px; line-height: 19.3px; text-align: justify; color: var(--ink); }
  .letter-body p { text-indent: 14px; }
  .letter-body p + p { margin-top: 19.3px; }
  .sign-off { margin: 16px 0 0 384px; font-size: 10.5px; line-height: 14px; color: var(--ink); }
  .sign-off .script { font-family: "Allura", cursive; font-size: 17px; line-height: 20px; color: var(--script); margin: 6px 0 3px 4px; }

  /* Envelope front */
  .envelope-front { left: 606px; top: 28px; width: 544px; height: 255px; }
  .envelope-front .brand-name { left: 34px; top: 30px; font-size: 52px; }
  .envelope-front .contact { left: 216px; top: 28px; }
  .address-window {
    position: absolute; left: 35px; top: 117px; width: 206px; height: 65px;
    border: 1px solid var(--rule); border-radius: 9px;
  }
  .envelope-front .band-bottom { top: 225px; height: 13px; }

  /* Envelope back */
  .envelope-back { left: 606px; top: 349px; width: 544px; height: 257px; }
  .envelope-back .flap { position: absolute; left: 0; top: 0; width: 544px; height: 75px; }
  .envelope-back .brand-name { left: 0; right: 0; top: 160px; font-size: 31px; text-align: center; }
</style>
</head>
<body>

<svg width="0" height="0" style="position:absolute">
  <defs>
    <symbol id="icon-phone" viewBox="0 0 10 10"><path d="M2 0.8 L3.6 2.8 L2.8 3.8 Q3.8 5.8 6 7 L7 6.2 L9 7.8 L8 9.4 Q3 9 0.8 2 Z" fill="#2b2b2b"/></symbol>
    <symbol id="icon-pin" viewBox="0 0 10 10"><path d="M5 9.6 L2 5.4 A3.4 3.4 0 1 1 8 5.4 Z" fill="#2b2b2b"/><circle cx="5" cy="3.6" r="1.3" fill="#fff"/></symbol>
    <symbol id="icon-mail" viewBox="0 0 10 10"><rect x="0.7" y="2" width="8.6" height="6" fill="none" stroke="#2b2b2b" stroke-width="0.9"/><path d="M0.7 2 L5 5.6 L9.3 2" fill="none" stroke="#2b2b2b" stroke-width="0.9"/></symbol>
    <symbol id="icon-web" viewBox="0 0 10 10"><circle cx="5" cy="5" r="4.2" fill="none" stroke="#2b2b2b" stroke-width="0.9"/><ellipse cx="5" cy="5" rx="1.8" ry="4.2" fill="none" stroke="#2b2b2b" stroke-width="0.8"/><path d="M0.8 5 H9.2" stroke="#2b2b2b" stroke-width="0.8"/></symbol>
  </defs>
</svg>

<section class="sheet letterhead">
  <div class="band band-top"></div>
  <div class="brand-name">vardel</div>
  <ul class="contact">
    <li><span class="bar"></span><svg><use href="#icon-phone"/></svg>555-210-4830</li>
    <li><span class="bar"></span><svg><use href="#icon-pin"/></svg>418 Linden Row&nbsp;&nbsp;&nbsp;Bay Area&nbsp;&nbsp;&nbsp;CA-75021</li>
    <li><span class="bar"></span><svg><use href="#icon-mail"/></svg>info@vardel.com</li>
    <li><span class="bar"></span><svg><use href="#icon-web"/></svg>www.vardel.com</li>
  </ul>
  <div class="letter-content">
    <div class="letter-body">
      <p>Lorem ipsum dolor sit amet, consectetuer adipiscing elit. Aenean commodo ligula eget dolor. Aenean massa. Cum sociis natoque penatibus et magnis dis parturient montes, nascetur ridiculus mus. Donec quam felis, ultricies nec, pellentesque eu, pretium quis, sem. Nulla consequat massa quis enim. Donec pede justo, fringilla vel, aliquet nec, vulputate eget, arcu. In enim justo, rhoncus ut, imperdiet a, venenatis vitae, justo. Nullam dictum felis eu pede mollis pretium. Integer tincidunt. Cras dapibus. Vivamus elementum semper nisi.</p>
      <p>Integer tincidunt. Cras dapibus. Vivamus elementum semper nisi. Aenean vulputate eleifend tellus. Aenean leo ligula, porttitor eu, consequat vitae, eleifend ac, enim. Aliquam lorem ante, dapibus in, viverra quis, feugiat a, tellus. Phasellus viverra nulla ut metus varius laoreet. Quisque rutrum. Aenean imperdiet. Etiam ultricies nisi vel augue. Curabitur ullamcorper ultricies nisi. Nam eget dui. Etiam rhoncus. Maecenas tempus, tellus eget condimentum rhoncus, sem quam semper libero, sit amet adipiscing sem neque sed ipsum. Nam quam nunc, blandit vel, luctus pulvinar, hendrerit id, lorem. Maecenas nec odio et ante tincidunt tempus. Donec vitae sapien ut libero venenatis faucibus. Nullam quis ante. Etiam sit amet orci eget eros faucibus tincidunt. Duis leo. Sed fringilla mauris sit amet nibh. Donec sodales sagittis magna. Sed consequat, leo eget bibendum sodales, augue velit cursus nunc, Vestibulum volutpat pretium libero. Cras id dui. Aenean ut</p>
    </div>
    <div class="sign-off">
      <div>yours sincerely</div>
      <div class="script">John Doe</div>
      <div>JOHN DOE</div>
    </div>
  </div>
  <div class="band band-bottom"></div>
</section>

<section class="sheet envelope-front">
  <div class="brand-name">vardel</div>
  <ul class="contact">
    <li><span class="bar"></span><svg><use href="#icon-phone"/></svg>555-210-4830</li>
    <li><span class="bar"></span><svg><use href="#icon-pin"/></svg>418 Linden Row&nbsp;&nbsp;&nbsp;Bay Area&nbsp;&nbsp;&nbsp;CA-75021</li>
    <li><span class="bar"></span><svg><use href="#icon-mail"/></svg>info@vardel.com</li>
    <li><span class="bar"></span><svg><use href="#icon-web"/></svg>www.vardel.com</li>
  </ul>
  <div class="address-window"></div>
  <div class="band band-bottom"></div>
</section>

<section class="sheet envelope-back">
  <svg class="flap" viewBox="0 0 544 75" preserveAspectRatio="none">
    <path d="M0 0 L28 73 L516 73 L544 0" fill="none" stroke="#bdbdbd" stroke-width="1.2"/>
  </svg>
  <div class="brand-name">vardel</div>
</section>

</body>
</html>
```